Equipment Finance Specialist I work with companies who need the funds to buy their equipment

I would like a business card that stands out on the shelves. I want to be able to hand it to someone and say WOW. This card should have my logo.
You can put color into it I am very open on design and color

What my company does is we deal with dealerships that sell equipment such as Dump Trucks garbage trucks tractors trailers. Customers get referred to us and depending on their time in business we will ask for the following items

Companies that have been in business for more than two years we have a credit application program up to 250K . With this program we need the following items Credit application filled out(which is what I would like to be able for the customer to click on my website to get.) as well as three current month bank statements.

Deals over 250k we will need the following items

2 years business tax returns
2 years personal tax returns
Profit & Loss statement
Personal Financial Statement

what we do
100% FINANCING
SEASONAL PAYMENTS
LOAN BALLOON PAYMENTS
TRAC LEASING
LOW-INTEREST REFINANCING RATES
DEBT CONSOLIDATION

We specialize in creative financing solutions and offer a variety of reliable, flexible and expandable lending choices.

Target Market(s)

Trucking Companies

Industry/Entity Type

Trucking Company

Contact Information for Business Card

* $250,000 Application only Program
* Loans from $30,000 to 5,000,000
* Competitive Interest Rates

Font styles to use
Serif
Sans Serif

Colors

Designer to choose colors to be used in the design.

Requirements
Must have
• On the back of the card.
• * $250,000 Application only Program
• * Loans from $30,000 to 5,000,000
• My name, email, website. address
• * Competitive Interest Rates
• * 100% Financing
Nice to have
• I want my logo to pop on the card
• My logo is the great one I would like to use
Should not have
• I am up for your creativity as well

```html
<!DOCTYPE html>
<html lang="en">
<head>
<meta charset="utf-8">
<title>Ridgeline Capital — Business Card</title>
<link href="https://fonts.googleapis.com/css2?family=Michroma&family=Saira:wght@500&family=Source+Sans+3:wght@400;700&display=swap" rel="stylesheet">
<style>
  :root {
    --page: #e4e4e4;
    --card-front: #ffffff;
    --card-back: #17191c;
    --navy: #122b6b;
    --navy-soft: #2c4a90;
    --red: #d3213a;
    --grey-text: #6a6d72;
    --silver: #d4d6d9;
    --white: #ffffff;
  }
  * { margin: 0; padding: 0; box-sizing: border-box; }
  html, body {
    width: 1125px; height: 1200px; overflow: hidden;
    background: var(--page);
  }
  .card {
    position: absolute;
    left: 150px;
    width: 825px;
    height: 471px;
  }
  .card-front { top: 98px; background: var(--card-front); }
  .card-back { top: 631px; background: var(--card-back); }

  .boom-illustration {
    position: absolute;
    left: 0; top: 22px;
    width: 350px; height: 428px;
    background: linear-gradient(160deg, var(--navy) 0%, var(--navy-soft) 100%);
  }

  .contact-block {
    position: absolute;
    right: 46px; top: 200px;
    text-align: right;
  }
  .holder-name {
    font-family: "Michroma", sans-serif;
    font-size: 25px;
    color: var(--navy);
    line-height: 1;
    letter-spacing: 0.5px;
  }
  .holder-title {
    font-family: "Michroma", sans-serif;
    font-size: 17px;
    color: var(--red);
    margin-top: 8px;
    line-height: 1;
  }
  .address {
    font-family: "Saira", sans-serif;
    font-weight: 500;
    font-size: 19px;
    color: var(--grey-text);
    line-height: 26px;
    margin-top: 26px;
  }
  .contact-lines { list-style: none; margin-top: 13px; }
  .contact-lines li {
    font-family: "Saira", sans-serif;
    font-weight: 500;
    font-size: 18px;
    color: var(--grey-text);
    line-height: 27px;
    display: flex;
    justify-content: flex-end;
    align-items: center;
    gap: 10px;
  }
  .contact-lines .phone { font-size: 20px; }
  .contact-lines svg { width: 18px; height: 18px; fill: var(--navy); flex: none; }

  .brand {
    position: absolute;
    left: 0; right: 0; top: 178px;
    display: flex;
    justify-content: center;
    align-items: center;
    gap: 20px;
  }
  .brand-dot {
    width: 72px; height: 72px;
    border-radius: 50%;
    background: var(--silver);
  }
  .brand-name {
    font-family: "Source Sans 3", sans-serif;
    font-weight: 700;
    color: var(--silver);
    font-size: 52px;
    line-height: 1;
    letter-spacing: 2px;
  }
  .offer-lines {
    position: absolute;
    left: 0; right: 0; top: 384px;
    text-align: center;
    font-family: "Source Sans 3", sans-serif;
    font-size: 20px;
    color: var(--white);
    line-height: 26px;
  }
</style>
</head>
<body>
  <section class="card card-front">
    <div class="boom-illustration" role="img" aria-label="Navy illustration of a crane boom with hook and lifting chains"></div>
    <div class="contact-block">
      <h1 class="holder-name">MARCUS HALE</h1>
      <p class="holder-title">PRESIDENT</p>
      <address class="address">4127 Harbor Point Road<br>Maple Grove, NY 11420</address>
      <ul class="contact-lines">
        <li class="phone">555 0148 2276
          <svg viewBox="0 0 24 24" aria-hidden="true"><path d="M6.6 10.8a15.1 15.1 0 0 0 6.6 6.6l2.2-2.2a1 1 0 0 1 1-.25 11.4 11.4 0 0 0 3.6.57 1 1 0 0 1 1 1V20a1 1 0 0 1-1 1A17 17 0 0 1 3 4a1 1 0 0 1 1-1h3.5a1 1 0 0 1 1 1c0 1.25.2 2.45.57 3.57a1 1 0 0 1-.25 1z"/></svg>
        </li>
        <li>marcus@ridgelinecap.com
          <svg viewBox="0 0 24 24" aria-hidden="true"><path d="M2 6h20v12H2z M2 6l10 7 10-7" fill="var(--navy)"/><path d="M2 6l10 7 10-7" fill="none" stroke="#fff" stroke-width="1.5"/></svg>
        </li>
        <li>www.ridgelinecap.com
          <svg viewBox="0 0 24 24" aria-hidden="true"><circle cx="12" cy="12" r="10"/></svg>
        </li>
      </ul>
    </div>
  </section>

  <section class="card card-back">
    <div class="brand">
      <span class="brand-dot" aria-hidden="true"></span>
      <span class="brand-name">RIDGELINE CAPITAL</span>
    </div>
    <div class="offer-lines">
      <p>$250,000 Application only Program ● Loans from $30,000 to 5,000,000</p>
      <p>Competitive Interest Rates ● 100% Financing</p>
    </div>
  </section>
</body>
</html>
```